Verpackungen für ein Standbodenbeutel Doypack
Zielgruppe
Wir betreiben eine eigene Öl-Manufaktur und bieten ausschließlich natureine Speiseöle und Tierprodukte - Superfood pulver.
Aufgabenstellung
Es wird auf einen Standbodenbeutel Doypack (braun) gedruckt. Es handelt sich um das Produkt Bio Hagebuttenpulver
Es sollte Naturel aussehen , was auf dem Packung stehen sollte u.a.
Schonend gemahlen
100% Vegan
100% natürlich
Ohne Zusatzstoffe
Verzehrempfehlung : Täglich 2 Teelöffel Bio Hagebuttenpulver nach Wunsch einnehmen.
Nährwert Tabelle
Eine Vorlage wurde vom Standbeutel wurde hochgeladen, auch das Firmen Logo wurde hochgeladen.
Die Datei sollteals Adobe Ai und ID
Bei Rückfragen einfach anschfreiben.

```html
<!DOCTYPE html>
<html lang="de">
<head>
<meta charset="utf-8">
<title>Wildhain – Bio Hagebuttenpulver Standbodenbeutel</title>
<link rel="stylesheet" href="https://fonts.googleapis.com/css2?family=Amatic+SC:wght@700&family=Source+Sans+3:wght@400;600;700&display=swap">
<style>
  :root{
    --kraft:#c7a780;
    --kraft-light:#cfb08b;
    --kraft-dark:#b8976f;
    --frame-green:#5e9c40;
    --brand-green:#4a8a37;
    --headline-teal:#2f8a72;
    --pill-green:#3f9a42;
    --pill-light:#7fbf55;
    --pill-text:#e6f1cf;
    --copy-green:#5f9a36;
    --ink:#4b4034;
    --page-white:#ffffff;
    --stage-grey:#dcdcdc;
  }
  *{box-sizing:border-box;margin:0;padding:0}
  html,body{width:1200px;height:1200px;overflow:hidden}
  body{position:relative;background:var(--page-white);font-family:"Source Sans 3",sans-serif}

  .stage{position:absolute;left:587px;width:613px;height:600px;background:var(--stage-grey)}
  .stage--top{top:0}
  .stage--bottom{top:600px}

  .pouch{
    position:absolute;width:340px;height:462px;
    background:
      radial-gradient(circle at 30% 20%, var(--kraft-light), transparent 60%),
      radial-gradient(circle at 75% 80%, var(--kraft-dark), transparent 65%),
      var(--kraft);
  }
  .pouch__seal{position:absolute;left:0;right:0;top:40px;height:5px;border-top:1px solid rgba(120,100,80,.35);border-bottom:1px solid rgba(120,100,80,.35)}

  .label{position:absolute;border:1.5px solid var(--frame-green);border-radius:5px;outline:1px solid var(--frame-green);outline-offset:-4px;text-align:center}
  .label--front{left:53px;top:82px;width:232px;height:301px}
  .label--back{left:110px;top:81px;width:121px;height:301px}

  .brand{position:absolute;left:0;right:0;display:flex;justify-content:center;align-items:center;gap:4px;color:var(--brand-green);font-weight:600}
  .brand__dot{width:8px;height:8px;border-radius:50%;background:var(--brand-green)}
  .label--front .brand{top:36px;font-size:14px}
  .label--back .brand{bottom:12px;font-size:9px}
  .label--back .brand__dot{width:6px;height:6px}

  .bio-pill{position:absolute;background:var(--pill-green);border-radius:50%;color:var(--pill-text);font-weight:400;display:flex;align-items:center;justify-content:center;box-shadow:6px 3px 0 -1px var(--pill-light)}
  .label--front .bio-pill{left:47px;top:74px;width:60px;height:30px;font-size:18px}
  .label--back .bio-pill{left:25px;top:10px;width:30px;height:16px;font-size:10px;box-shadow:3px 2px 0 -1px var(--pill-light)}

  .headline{position:absolute;left:0;right:0;font-family:"Amatic SC",cursive;color:var(--headline-teal);line-height:.95;letter-spacing:1px}
  .label--front .headline{top:100px;font-size:46px}
  .label--back .headline{top:26px;font-size:22px}

  .claims{position:absolute;left:0;right:0;color:var(--copy-green);font-weight:600;line-height:1.25}
  .label--front .claims{top:264px;font-size:7.5px;padding-left:40px;transform:rotate(-1deg)}
  .label--back .claims{top:80px;font-size:6.5px}

  .illustration{position:absolute;border-radius:40% 45% 35% 40%;background:radial-gradient(ellipse at center, rgba(75,64,52,.35), rgba(75,64,52,.08) 70%, transparent)}
  .label--front .illustration{left:22px;top:182px;width:190px;height:84px}
  .label--back .illustration{left:14px;top:112px;width:93px;height:44px}

  .serving{position:absolute;left:8px;right:6px;top:184px;text-align:left;color:var(--copy-green);font-size:5px;font-weight:600;line-height:1.25}

  .nutrition{position:absolute;left:8px;right:8px;top:212px;border-collapse:collapse;font-size:3.2px;color:var(--ink);text-align:left}
  .nutrition th{font-weight:700;padding-bottom:1px}
  .nutrition td{border-bottom:.5px solid rgba(75,64,52,.5);padding:.4px 0}
  .nutrition td.value{text-align:right}
</style>
</head>
<body>

<div class="stage stage--top"></div>
<div class="stage stage--bottom"></div>

<!-- Front, flat -->
<section class="pouch" style="left:95px;top:67px">
  <div class="pouch__seal"></div>
  <div class="label label--front">
    <div class="brand"><span class="brand__dot"></span>Wildhain</div>
    <div class="bio-pill">BIO</div>
    <h1 class="headline">HAGEBUTTEN<br>PULVER</h1>
    <div class="illustration" role="img" aria-label="Strichzeichnung von Hagebutten mit Blättern"></div>
    <p class="claims">schonend gemalen – Ohne Zusatzstoffe<br>100% Vegan – 100% natürlich</p>
  </div>
</section>

<!-- Back, flat -->
<section class="pouch" style="left:95px;top:670px">
  <div class="pouch__seal"></div>
  <div class="label label--back">
    <div class="bio-pill">BIO</div>
    <h2 class="headline">HAGEBUTTEN<br>PULVER</h2>
    <p class="claims">schonend gemalen<br>ohne Zusatzstoffe<br>100% Vegan – 100% natürlich</p>
    <div class="illustration" role="img" aria-label="Strichzeichnung von Hagebutten mit Blättern"></div>
    <p class="serving">Verzehrempfehlung:<br>Täglich 2 Teelöffel Bio Hagebuttenpulver nach Wunsch einnehmen.</p>
    <table class="nutrition">
      <tr><th colspan="2">Durchschnittliche Nährwerte / Average nutritional value / Valore nutrizionale medi a100g</th></tr>
      <tr><td>Energie/Energy/Energia</td><td class="value">0000 kJ/000 kcal</td></tr>
      <tr><td>Fett/Fat/Grassi</td><td class="value">00 g</td></tr>
      <tr><td>davon gesättigte Fettsäuren/of which saturated fatty acids/di cui acidi grassi saturi</td><td class="value">00 g</td></tr>
      <tr><td>Kohlenhydrate/Carbohydrates/Carboidrati</td><td class="value">00 g</td></tr>
      <tr><td>davon Zucker/of which sugars/di cui zuccheri</td><td class="value">00 g</td></tr>
      <tr><td>Ballaststoffe/Dietary fibre/Fibra dietetica</td><td class="value">0,0 g</td></tr>
      <tr><td>Eiweiß/Protein/Proteine</td><td class="value">0 g</td></tr>
    </table>
    <div class="brand"><span class="brand__dot"></span>Wildhain</div>
  </div>
</section>

<!-- Front, presented -->
<section class="pouch" style="left:723px;top:70px">
  <div class="pouch__seal"></div>
  <div class="label label--front">
    <div class="brand"><span class="brand__dot"></span>Wildhain</div>
    <div class="bio-pill">BIO</div>
    <h1 class="headline">HAGEBUTTEN<br>PULVER</h1>
    <div class="illustration" role="img" aria-label="Strichzeichnung von Hagebutten mit Blättern"></div>
    <p class="claims">schonend gemalen – Ohne Zusatzstoffe<br>100% Vegan – 100% natürlich</p>
  </div>
</section>

<!-- Back, presented -->
<section class="pouch" style="left:723px;top:673px">
  <div class="pouch__seal"></div>
  <div class="label label--back">
    <div class="bio-pill">BIO</div>
    <h2 class="headline">HAGEBUTTEN<br>PULVER</h2>
    <p class="claims">schonend gemalen<br>ohne Zusatzstoffe<br>100% Vegan – 100% natürlich</p>
    <div class="illustration" role="img" aria-label="Strichzeichnung von Hagebutten mit Blättern"></div>
    <p class="serving">Verzehrempfehlung:<br>Täglich 2 Teelöffel Bio Hagebuttenpulver nach Wunsch einnehmen.</p>
    <table class="nutrition">
      <tr><th colspan="2">Durchschnittliche Nährwerte / Average nutritional value / Valore nutrizionale medi a100g</th></tr>
      <tr><td>Energie/Energy/Energia</td><td class="value">0000 kJ/000 kcal</td></tr>
      <tr><td>Fett/Fat/Grassi</td><td class="value">00 g</td></tr>
      <tr><td>davon gesättigte Fettsäuren/of which saturated fatty acids/di cui acidi grassi saturi</td><td class="value">00 g</td></tr>
      <tr><td>Kohlenhydrate/Carbohydrates/Carboidrati</td><td class="value">00 g</td></tr>
      <tr><td>davon Zucker/of which sugars/di cui zuccheri</td><td class="value">00 g</td></tr>
      <tr><td>Ballaststoffe/Dietary fibre/Fibra dietetica</td><td class="value">0,0 g</td></tr>
      <tr><td>Eiweiß/Protein/Proteine</td><td class="value">0 g</td></tr>
    </table>
    <div class="brand"><span class="brand__dot"></span>Wildhain</div>
  </div>
</section>

</body>
</html>
```